"Sun On Water" Gospel Presentation Booklet

I need a design for a 12 page (including front/back cover) square booklet, with religious images and aesthetically pleasing fonts/designs. I want it to be very simple, and very straightforward. The main focus of the project is it's content. So the design should be very nice, but also should point to the content, not take away from it, or create distraction. People should be more focused on the words than the imagery.

I enjoy modern designs, I need a sharp aesthetic that is clean and neat. Nothing over the top.
I have attached a word document with the content I would like on the pages.

Colors
0592cd
0255a3
33a6d7
85cae6
85acd3
3276b5
9bcb3b
f04a50
f68d4c

Requirements
Should not have
• Super feminine colors/aesthetics

```html
<!DOCTYPE html>
<html lang="en">
<head>
<meta charset="utf-8">
<title>Sun On Water – Gospel Booklet Spreads</title>
<link href="https://fonts.googleapis.com/css2?family=Playfair+Display:wght@700;800&family=Mulish:wght@400;600;800&display=swap" rel="stylesheet">
<style>
  :root {
    --bg: #f2f2f3;
    --paper: #f7f7f8;
    --navy: #1f2867;
    --navy-light: #333c8a;
    --royal: #1b3ea6;
    --royal-light: #2c55c4;
    --bright: #1c6fe0;
    --bright-light: #3d8cf0;
    --sky: #2e7fe0;
    --sky-light: #5aa0f0;
    --ink: #222;
    --frame-blue: #1b3ea6;
    --white: #ffffff;
  }
  * { margin: 0; padding: 0; box-sizing: border-box; }
  html, body { width: 1200px; height: 1000px; overflow: hidden; }
  body { background: var(--bg); font-family: "Mulish", Arial, sans-serif; position: relative; }

  .spread {
    position: absolute;
    width: 480px; height: 250px;
    display: flex;
    box-shadow: 0 10px 24px rgba(0,0,0,0.12);
  }
  .page {
    position: relative;
    width: 240px; height: 250px;
    display: flex; align-items: center; justify-content: center;
    background: var(--paper);
  }
  .page::after {
    content: ""; position: absolute; inset: 11px;
    border: 1.5px solid var(--frame-blue);
    pointer-events: none;
  }
  .page.dark::after { border-color: rgba(255,255,255,0.9); }

  .page.navy { background: linear-gradient(90deg, var(--navy), var(--navy-light) 75%, var(--navy)); }
  .page.royal { background: linear-gradient(90deg, var(--royal), var(--royal-light) 75%, var(--royal)); }
  .page.bright { background: linear-gradient(90deg, var(--bright-light), var(--bright)); }
  .page.sky { background: linear-gradient(90deg, var(--sky), var(--sky-light) 75%, var(--sky)); }

  .heading {
    font-family: "Playfair Display", Georgia, serif;
    font-weight: 800;
    font-size: 29px;
    letter-spacing: -0.5px;
    color: var(--white);
  }
  .heading.on-paper { color: var(--navy); }
  .heading.on-paper-bright { color: var(--bright); }

  .body-copy {
    width: 175px;
    font-size: 8.2px;
    line-height: 1.45;
    text-align: center;
    color: var(--ink);
  }
  .body-copy.light { color: var(--white); }
  .body-copy p + p { margin-top: 9px; }
  .body-copy .call {
    color: var(--bright);
    font-weight: 800;
  }

  .spread-god { left: 110px; top: 55px; }
  .spread-problem { left: 628px; top: 55px; }
  .spread-man { left: 110px; top: 352px; }
  .spread-christ { left: 628px; top: 352px; }
  .spread-response { left: 110px; top: 675px; }

  .cover {
    position: absolute; left: 740px; top: 672px;
    width: 255px; height: 255px;
    display: flex;
    box-shadow: 0 10px 24px rgba(0,0,0,0.15);
  }
  .cover-band {
    position: relative; width: 162px; height: 100%;
    background: linear-gradient(180deg, var(--navy-light), var(--navy));
  }
  .cover-title {
    position: absolute; left: 20px; bottom: 24px;
    font-family: "Playfair Display", Georgia, serif;
    font-weight: 800; font-size: 30px; line-height: 1.02;
    color: var(--white);
    letter-spacing: -0.5px;
  }
  .cover-photo {
    width: 93px; height: 100%;
    background: linear-gradient(180deg, #5a5a5a, #8a8a8a 45%, #2c2c2c);
  }
</style>
</head>
<body>

  <section class="spread spread-god">
    <div class="page dark navy"><h2 class="heading">GOD</h2></div>
    <div class="page">
      <div class="body-copy"><p>God is holy, that means He's perfect. In fact, He is so perfect, corruption cannot live with Him.</p></div>
    </div>
  </section>

  <section class="spread spread-problem">
    <div class="page dark royal"><h2 class="heading">PROBLEM</h2></div>
    <div class="page">
      <div class="body-copy"><p>And there is our big problem: if God is perfect and corruption cannot live with him....and we are corrupt..... WE cannot live with God. Our corruption has cut us off from God...now.....AND when we die which means we must spend eternity in a place called hell...</p></div>
    </div>
  </section>

  <section class="spread spread-man">
    <div class="page"><h2 class="heading on-paper">MAN</h2></div>
    <div class="page dark navy">
      <div class="body-copy light"><p>On the other hand, mankind is corrupt. For example, we are selfish, we are prideful, and we lie.</p></div>
    </div>
  </section>

  <section class="spread spread-christ">
    <div class="page"><h2 class="heading on-paper-bright">CHRIST</h2></div>
    <div class="page dark bright">
      <div class="body-copy light">
        <p>But that is not what God wants.</p>
        <p>God loves you so much he gave up his only Son to save you. Jesus Christ died on the cross in our place to pay for our sin and rose again on the 3rd day.</p>
      </div>
    </div>
  </section>

  <section class="spread spread-response">
    <div class="page dark sky"><h2 class="heading">RESPONSE</h2></div>
    <div class="page">
      <div class="body-copy">
        <p>So now if anyone:</p>
        <p>1. Agrees with God they are corrupt.</p>
        <p>2. Believes Jesus Christ will save them.</p>
        <p>3. And accepts Him as their personal Lord and Savior, Jesus Christ will forgive their corruption, reconcile them to God, and come and live inside them.</p>
        <p class="call">You can pray to Jesus Christ right now and ask him to save you using the above three steps as your prayer guide.</p>
      </div>
    </div>
  </section>

  <section class="cover">
    <div class="cover-band"><h1 class="cover-title">SUN ON<br>WATER...</h1></div>
    <div class="cover-photo" role="img" aria-label="Black and white photo of an open Bible held up against the sky with a small cross pendant hanging below"></div>
  </section>

</body>
</html>
```